hi all

Im after a new age looking business card with my company logo on it

must include these details, I would like the PH and Email to be symbols

If the colours used for card could be kept within the colours used in logo that I have supplied that would be great, if another colour is to be used dark grey would be ok. no light bulbs etc thanks

Details below to be incorporated on card

Damian Holloway

Lic E871302

PH 0219647381

E info@brightvaleelectrical.example.nz

Domestic Commercial Industrial Electricians

```html
<!DOCTYPE html>
<html lang="en">
<head>
<meta charset="UTF-8">
<title>Brightvale Electrical – Business Card</title>
<link href="https://fonts.googleapis.com/css2?family=Montserrat:wght@400;500;700;800&display=swap" rel="stylesheet">
<style>
  :root {
    --brand-blue: #0a75bc;
    --brand-blue-deep: #0866a6;
    --ink: #1a1a1a;
    --card-white: #ffffff;
    --stage: #d9dcdf;
  }
  * { margin: 0; padding: 0; box-sizing: border-box; }
  html, body { width: 1200px; height: 800px; overflow: hidden; }
  body {
    background: var(--stage);
    font-family: "Montserrat", sans-serif;
    color: var(--ink);
    position: relative;
  }
  .card {
    position: absolute;
    width: 600px;
    height: 340px;
    overflow: hidden;
    box-shadow: 0 6px 18px rgba(0,0,0,0.18);
  }
  .card-back {
    left: 460px;
    top: 44px;
    background: var(--brand-blue);
    display: flex;
    align-items: center;
    justify-content: center;
  }
  .back-mark {
    display: flex;
    align-items: center;
    gap: 18px;
  }
  .back-mark .dot {
    width: 70px; height: 70px;
    border-radius: 50%;
    background: var(--brand-blue-deep);
  }
  .back-mark .name {
    font-weight: 800;
    font-size: 34px;
    letter-spacing: 2px;
    color: var(--brand-blue-deep);
    text-transform: uppercase;
  }
  .card-front {
    left: 140px;
    top: 410px;
    background: var(--card-white);
  }
  .brand {
    position: absolute;
    left: 30px;
    top: 92px;
    width: 220px;
    display: flex;
    flex-direction: column;
    align-items: center;
    gap: 10px;
  }
  .brand .dot {
    width: 46px; height: 46px;
    border-radius: 50%;
    background: var(--brand-blue);
  }
  .brand .name {
    font-weight: 800;
    font-size: 24px;
    line-height: 1.05;
    letter-spacing: 1px;
    color: var(--brand-blue);
    text-transform: uppercase;
    text-align: center;
  }
  .divider {
    position: absolute;
    left: 268px;
    top: 72px;
    width: 3px;
    height: 124px;
    background: var(--brand-blue);
  }
  .contact {
    position: absolute;
    left: 290px;
    right: 20px;
    top: 78px;
  }
  .contact .person {
    font-weight: 700;
    font-size: 19px;
    color: var(--brand-blue);
  }
  .contact .role {
    font-size: 13px;
    margin-bottom: 14px;
  }
  .contact .line {
    display: flex;
    align-items: center;
    gap: 7px;
    font-size: 13px;
    line-height: 1.5;
    white-space: nowrap;
  }
  .contact .line svg { width: 12px; height: 12px; flex: none; }
  .tagline {
    position: absolute;
    left: 0; right: 0;
    bottom: 42px;
    text-align: center;
    font-size: 15px;
  }
</style>
</head>
<body>
  <section class="card card-back">
    <div class="back-mark">
      <span class="dot"></span>
      <span class="name">Brightvale</span>
    </div>
  </section>

  <section class="card card-front">
    <div class="brand">
      <span class="dot"></span>
      <span class="name">Brightvale<br>Electrical</span>
    </div>
    <div class="divider"></div>
    <div class="contact">
      <p class="person">Damian Holloway</p>
      <p class="role">Founder</p>
      <p class="line">
        <svg viewBox="0 0 24 24" aria-hidden="true"><path fill="#0a75bc" d="M6.6 10.8a15.1 15.1 0 0 0 6.6 6.6l2.2-2.2a1 1 0 0 1 1-.25 11.4 11.4 0 0 0 3.6.57 1 1 0 0 1 1 1V20a1 1 0 0 1-1 1A17 17 0 0 1 3 4a1 1 0 0 1 1-1h3.5a1 1 0 0 1 1 1c0 1.25.2 2.45.57 3.57a1 1 0 0 1-.25 1z"/></svg>
        0219647381
      </p>
      <p class="line">
        <svg viewBox="0 0 24 24" aria-hidden="true"><rect x="2" y="5" width="20" height="14" fill="none" stroke="#0a75bc" stroke-width="2"/><path d="M2 5l10 8 10-8M2 19l7-7M22 19l-7-7" fill="none" stroke="#0a75bc" stroke-width="2"/></svg>
        info@brightvaleelectrical.example.nz
      </p>
      <p class="line">Lic E871302</p>
    </div>
    <p class="tagline">Domestic Commercial Industrial Electricians</p>
  </section>
</body>
</html>
```